DOUBLE SIDED BROCHURE NEEDED TO PROMOTE DOCTOR

I need a double sided DL size (99mm x 210mm) brochure, promoting a doctor seeing patients in a new area.

I want something professional. I have included the relevant information. I would also like the Dr's picture somwhere in the brochure, with a professional background. I wish to print these tomorrow, so i will pick a winner within 14 hours of posting this ad.

I have included an example of a brochures design that I recently saw, and its definietly a good starting point.

Medical

```html
<!DOCTYPE html>
<html lang="en">
<head>
<meta charset="utf-8">
<title>Dr. Karim Nasser – DL Brochure</title>
<link href="https://fonts.googleapis.com/css2?family=Bebas+Neue&family=Exo+2:ital,wght@1,700&family=Open+Sans:wght@300;400;600;700&display=swap" rel="stylesheet">
<style>
  :root{
    --backdrop:#3a0e1b;
    --blue:#2f86e0;
    --blue-deep:#1f6fcf;
    --blue-light:#4aa2ee;
    --teal:#5ec9c6;
    --green:#8ee617;
    --orange:#ff7a10;
    --navy:#153646;
    --white:#ffffff;
    --muted:#c9ddf2;
  }
  *{margin:0;padding:0;box-sizing:border-box}
  html,body{width:1200px;height:1200px;overflow:hidden;background:var(--backdrop)}
  .canvas{position:relative;width:1200px;height:1200px}
  .panel{position:absolute;top:119px;width:488px;height:1035px;overflow:hidden;
    background:linear-gradient(180deg,var(--blue-light) 0%,var(--blue) 45%,var(--blue-deep) 100%);
    font-family:"Open Sans",sans-serif;color:var(--white)}
  .panel--front{left:70px}
  .panel--back{left:634px}
  .abs{position:absolute}

  /* front */
  .hero-photo{left:0;top:0;width:488px;height:480px;
    background:linear-gradient(180deg,#6fa7e6 0%,#cfe0f2 35%,#8d949e 65%,#3c4450 100%)}
  .letter{font-family:"Exo 2",sans-serif;font-style:italic;font-weight:700;font-size:17.5px;
    line-height:23px;letter-spacing:.6px;word-spacing:3px;left:49px;width:410px}
  .clinic-box{left:78px;top:758px;width:335px;height:119px;background:var(--navy);text-align:center;padding-top:6px}
  .clinic-box__name{font-weight:700;font-size:26px;text-decoration:underline;text-underline-offset:4px}
  .clinic-box__line{font-weight:600;font-size:20px;line-height:31px}
  .clinic-box__name+.clinic-box__line{margin-top:10px}
  .phone-band{left:0;top:894px;width:488px;height:64px;background:var(--orange);display:flex;align-items:center;padding-left:32px}
  .phone-band__text{font-family:"Bebas Neue",sans-serif;font-size:46px;margin-left:20px;padding-top:4px}
  .fax-band{left:0;top:958px;width:488px;height:77px;background:var(--navy);text-align:center}
  .fax-band__label{font-weight:300;font-size:19px;margin-top:5px}
  .fax-band__number{font-weight:700;font-size:36px;line-height:40px}

  /* back */
  .title-band{left:0;top:0;width:488px;height:73px;background:var(--orange);text-align:center;
    font-family:"Bebas Neue",sans-serif;font-size:44px;line-height:80px}
  .teal-wash{left:0;top:73px;width:488px;height:400px;
    background:linear-gradient(160deg,var(--teal) 0%,#4fb3cf 55%,var(--blue-light) 100%)}
  .intro{left:54px;top:436px;width:420px;font-size:20.5px;line-height:25px}
  .service{font-size:20px;line-height:24px;left:114px;width:340px}
  .service__note{color:var(--muted)}
  .tick{position:absolute;left:-27px;top:5px}
  .subhead{left:60px;top:734px;font-size:20.5px}
</style>
</head>
<body>
<div class="canvas">

  <section class="panel panel--front">
    <div class="abs hero-photo" role="img" aria-label="Portrait of the surgeon in a suit in front of a modern hospital building under a blue sky"></div>
    <svg class="abs" style="left:0;top:0" width="488" height="1035" viewBox="0 0 488 1035" aria-hidden="true">
      <path d="M0 401 Q250 470 488 389 L488 1035 L0 1035 Z" fill="var(--green)"/>
      <path d="M0 417 Q260 500 488 449 L488 1035 L0 1035 Z" fill="var(--blue-light)"/>
    </svg>
    <div class="abs letter" style="top:467px">Dear Doctors,</div>
    <p class="abs letter" style="top:507px">We are pleased to announce that Dr. Karim Nasser is now consulting in Coralbay, seeing public and private patients.</p>
    <p class="abs letter" style="top:622px">Guaranteed appointment within two weeks, with patients having the option of surgery at Harbour Health Campus, Westbrook Hospital or St. Aldric's Lakeside.</p>
    <div class="abs clinic-box">
      <div class="clinic-box__name">Coralbay Clinic</div>
      <div class="clinic-box__line">42 Kestrel Road</div>
      <div class="clinic-box__line">Coralbay WA 6999.</div>
    </div>
    <div class="abs phone-band">
      <svg width="32" height="24" viewBox="0 0 32 24" aria-hidden="true">
        <path d="M2 9 Q16 0 30 9 L27 13 L22 11 L22 8 Q16 6 10 8 L10 11 L5 13 Z" fill="var(--white)"/>
        <path d="M9 13 L23 13 L27 23 L5 23 Z" fill="var(--white)"/>
        <circle cx="16" cy="18" r="3" fill="var(--orange)"/>
      </svg>
      <span class="phone-band__text">Phone - 1300 555 014</span>
    </div>
    <div class="abs fax-band">
      <div class="fax-band__label">Please send all referrals by fax to</div>
      <div class="fax-band__number">(08) 5550 7341</div>
    </div>
  </section>

  <section class="panel panel--back">
    <div class="abs teal-wash" role="img" aria-label="Soft teal medical texture background"></div>
    <svg class="abs" style="left:0;top:0" width="488" height="1035" viewBox="0 0 488 1035" aria-hidden="true">
      <defs><clipPath id="portrait-clip"><circle cx="406" cy="217" r="208"/></clipPath></defs>
      <path d="M0 380 Q200 470 488 420 L488 1035 L0 1035 Z" fill="var(--blue-light)"/>
      <circle cx="406" cy="217" r="211" fill="none" stroke="var(--blue-deep)" stroke-width="5"/>
    </svg>
    <div class="abs" style="left:198px;top:9px;width:416px;height:416px;border-radius:50%;
      background:linear-gradient(180deg,#a9c8ea 0%,#dbe6f1 40%,#6d7480 75%,#2a3240 100%)"
      role="img" aria-label="Circular portrait of the surgeon outside a hospital"></div>
    <div class="abs title-band">About Dr. Karim Nasser</div>

    <p class="abs intro">Dr. Nasser is a highly trained specialised surgeon, in all areas of Endocrine, Breast and General Surgery. Including;</p>

    <div class="abs service" style="top:530px"><svg class="tick" width="18" height="14" viewBox="0 0 18 14"><path d="M2 7 L7 12 L16 2" fill="none" stroke="#fff" stroke-width="2.4"/></svg>Thyroid Surgery</div>
    <div class="abs service" style="top:562px"><svg class="tick" width="18" height="14" viewBox="0 0 18 14"><path d="M2 7 L7 12 L16 2" fill="none" stroke="#fff" stroke-width="2.4"/></svg>Parathyroid surgery<br><span class="service__note">(including minimally invasive parathyroidectomy)</span></div>
    <div class="abs service" style="top:638px"><svg class="tick" width="18" height="14" viewBox="0 0 18 14"><path d="M2 7 L7 12 L16 2" fill="none" stroke="#fff" stroke-width="2.4"/></svg>Breast Cancer</div>
    <div class="abs service" style="top:669px"><svg class="tick" width="18" height="14" viewBox="0 0 18 14"><path d="M2 7 L7 12 L16 2" fill="none" stroke="#fff" stroke-width="2.4"/></svg>Benign breast lesions</div>

    <div class="abs subhead">All areas of general surgery, such as;</div>

    <div class="abs service" style="top:774px"><svg class="tick" width="18" height="14" viewBox="0 0 18 14"><path d="M2 7 L7 12 L16 2" fill="none" stroke="#fff" stroke-width="2.4"/></svg>Gallbladder surgery</div>
    <div class="abs service" style="top:807px"><svg class="tick" width="18" height="14" viewBox="0 0 18 14"><path d="M2 7 L7 12 L16 2" fill="none" stroke="#fff" stroke-width="2.4"/></svg>Hernia surgery</div>
    <div class="abs service" style="top:841px"><svg class="tick" width="18" height="14" viewBox="0 0 18 14"><path d="M2 7 L7 12 L16 2" fill="none" stroke="#fff" stroke-width="2.4"/></svg>Haemorrhoids</div>
    <div class="abs service" style="top:872px"><svg class="tick" width="18" height="14" viewBox="0 0 18 14"><path d="M2 7 L7 12 L16 2" fill="none" stroke="#fff" stroke-width="2.4"/></svg>Carpal Tunnel</div>
    <div class="abs service" style="top:902px"><svg class="tick" width="18" height="14" viewBox="0 0 18 14"><path d="M2 7 L7 12 L16 2" fill="none" stroke="#fff" stroke-width="2.4"/></svg>Vasectomy etc etc...</div>

    <svg class="abs" style="left:0;top:930px" width="488" height="105" viewBox="0 0 488 105" aria-hidden="true">
      <path d="M0 20 Q244 70 488 20 L488 105 L0 105 Z" fill="var(--white)"/>
      <path d="M0 30 Q244 80 488 30 L488 105 L0 105 Z" fill="var(--orange)"/>
    </svg>
  </section>

</div>
</body>
</html>
```